Hi,

I have just started up a business called VELUMO in Melbourne. We run fun street art tours around Melbourne's CBD.

I need to create a design for the back side of my business cards. I have designed the front side (simply with my logo) however, I am having trouble designing the reverse side in a professional manner. I have attached pictures of what I have done.

The picture attached titled "VELUMO Business Cards Back" has all the information that I require on the back side of my business cards; although displayed in an amateur and simple way. As displayed in the picture, I need: the VELUMO logo, the website URL, the booking details (phone - 0481 556 217 & email - bookings@velumo.com.au) and the service description ($20, One Hour, Tours Daily, Meet at Carrow Rd Terminal). I would also like to use the font in the picture supplied which is "source-sans-pro".

The VELUMO tours are for tourists and are relaxed, entertaining and fun! I would like the design to reflect this.

Target Market(s)

Backpackers & University Students

Industry/Entity Type

Business

Requirements
Must have
• The VELUMO logo, the website URL, the booking details (phone - 0481 556 217 & email - bookings@velumo.com.au) and the service description ($20, One Hour, Tours Daily, Meet at Carrow Rd Terminal).

```html
<!DOCTYPE html>
<html lang="en">
<head>
<meta charset="utf-8">
<title>VELUMO Business Cards</title>
<link href="https://fonts.googleapis.com/css2?family=Source+Sans+3:wght@400;600;700;800&display=swap" rel="stylesheet">
<style>
  :root{
    --page:#e9e9e9;
    --card:#ffffff;
    --ink:#1a1a1a;
    --red:#e0231d;
    --red-dark:#b3140f;
    --grey-text:#555a60;
    --pill-top:#f4f4f4;
    --pill-bottom:#d6d6d6;
  }
  *{box-sizing:border-box;margin:0;padding:0}
  html,body{width:1200px;height:847px;overflow:hidden}
  body{
    background:var(--page);
    font-family:"Source Sans 3",Arial,sans-serif;
    color:var(--ink);
    position:relative;
  }
  .card{
    position:absolute;
    top:92px;
    width:380px;
    height:664px;
    background:var(--card);
    box-shadow:0 6px 18px rgba(0,0,0,.12);
  }
  .card--back{left:170px}
  .card--front{left:650px}

  /* back card */
  .url-ribbon{
    position:absolute;left:36px;top:40px;width:308px;height:44px;
  }
  .url-ribbon svg{position:absolute;inset:0}
  .url-ribbon span{
    position:absolute;inset:0;display:flex;align-items:center;justify-content:center;
    color:#fff;font-weight:700;font-size:21px;letter-spacing:.3px;
  }
  .brand{
    display:flex;align-items:center;gap:12px;
    font-weight:800;color:var(--red);letter-spacing:2px;
  }
  .brand__dot{background:var(--red);border-radius:50%}
  .card--back .brand{position:absolute;top:118px;left:0;right:0;justify-content:center;font-size:52px}
  .card--back .brand__dot{width:22px;height:22px}

  .offer{
    position:absolute;top:212px;left:0;right:0;
    display:flex;flex-direction:column;align-items:center;
    font-weight:700;font-size:31px;line-height:1.05;text-align:center;
  }
  .offer .hl{color:var(--red)}
  .offer__arrow{width:14px;height:24px;margin:3px 0}
  .offer__meet{line-height:1.05}

  .book-pill{
    position:absolute;left:44px;top:510px;width:292px;height:44px;
    background:linear-gradient(var(--pill-top),var(--pill-bottom));
    border-radius:4px;
    box-shadow:0 2px 4px rgba(0,0,0,.18);
    display:flex;align-items:center;justify-content:center;
    font-weight:700;font-size:22px;
  }
  .book-pill .hl{color:var(--red);margin-left:6px}

  .contact{
    position:absolute;left:0;right:0;
    display:flex;align-items:center;justify-content:center;gap:10px;
    color:var(--grey-text);font-size:20px;font-weight:600;letter-spacing:.4px;
  }
  .contact--phone{top:570px}
  .contact--email{top:608px}
  .contact svg{width:22px;height:22px;flex:none}

  /* front card */
  .front-stack{
    position:absolute;inset:0;
    display:flex;justify-content:center;align-items:center;
    writing-mode:vertical-rl;
    gap:34px;
  }
  .card--front .brand{font-size:76px;letter-spacing:4px}
  .card--front .brand__dot{width:30px;height:30px}
  .tagline{
    font-weight:700;font-size:40px;line-height:1.1;text-align:center;color:var(--ink);
  }
</style>
</head>
<body>

<section class="card card--back" aria-label="Card back">
  <div class="url-ribbon">
    <svg viewBox="0 0 308 44" preserveAspectRatio="none" aria-hidden="true">
      <polygon points="0,6 20,6 14,25 20,44 0,44" fill="var(--red-dark)"/>
      <polygon points="308,6 288,6 294,25 288,44 308,44" fill="var(--red-dark)"/>
      <rect x="12" y="0" width="284" height="38" fill="var(--red)"/>
    </svg>
    <span>www.velumo.com.au</span>
  </div>

  <div class="brand"><span class="brand__dot"></span>VELUMO</div>

  <div class="offer">
    <div class="hl">$20</div>
    <svg class="offer__arrow" viewBox="0 0 14 24" aria-hidden="true"><path d="M7 0v16" stroke="var(--red)" stroke-width="3"/><path d="M0 14h14L7 24z" fill="var(--red)"/></svg>
    <div><span class="hl">Tours</span> Daily</div>
    <svg class="offer__arrow" viewBox="0 0 14 24" aria-hidden="true"><path d="M7 0v16" stroke="var(--red)" stroke-width="3"/><path d="M0 14h14L7 24z" fill="var(--red)"/></svg>
    <div><span class="hl">One</span> Hour</div>
    <svg class="offer__arrow" viewBox="0 0 14 24" aria-hidden="true"><path d="M7 0v16" stroke="var(--red)" stroke-width="3"/><path d="M0 14h14L7 24z" fill="var(--red)"/></svg>
    <div class="offer__meet">Meet at Carrow Rd<br><span class="hl">Terminal</span></div>
  </div>

  <div class="book-pill">Call Jai to <span class="hl">BOOK NOW</span></div>

  <div class="contact contact--phone">
    <svg viewBox="0 0 22 22" aria-hidden="true"><circle cx="11" cy="11" r="10" fill="none" stroke="var(--red)" stroke-width="1.6"/><path d="M7.5 6.5l2 0 .8 2.4-1.3 1c.7 1.4 1.7 2.4 3.1 3.1l1-1.3 2.4.8v2c-4.5.3-8.3-3.5-8-8z" fill="var(--red)"/></svg>
    0481 556 217
  </div>
  <div class="contact contact--email">
    <svg viewBox="0 0 22 22" aria-hidden="true"><circle cx="11" cy="11" r="10" fill="none" stroke="var(--red)" stroke-width="1.6"/><rect x="5.5" y="7.5" width="11" height="7.5" fill="none" stroke="var(--red)" stroke-width="1.4"/><path d="M5.5 7.5l5.5 4.5 5.5-4.5" fill="none" stroke="var(--red)" stroke-width="1.4"/></svg>
    bookings@velumo.com.au
  </div>
</section>

<section class="card card--front" aria-label="Card front">
  <div class="front-stack">
    <div class="brand"><span class="brand__dot"></span>VELUMO</div>
    <p class="tagline">Melbourne Street Art<br>Walking Tours</p>
  </div>
</section>

</body>
</html>
```